Brightlane Pixel Collective Website

I need my website redesigned to look very modern with the latest services. Check out my old website for information: www.brightlanepixelcollective.com

You can use the same site menu links

It doesn't need to have the Recent News section

Please use the yellow, black and grey color scheme
Updates

This project is now payment guaranteed. Lets see what everyone can do!

Target Market(s)

25-50 years in range. Small Business Owners

Industry/Entity Type

Group

Requirements
Must have
• Logo and similar color scheme to current website
• Modern, Modern, Modern! I want a very fresh and modern look
Should not have
• Boring Look

```html
<!DOCTYPE html>
<html lang="en">
<head>
<meta charset="utf-8">
<title>Brightlane Pixel Collective</title>
<link href="https://fonts.googleapis.com/css2?family=Exo:wght@500;600;700&family=Ubuntu:wght@400;500;700&display=swap" rel="stylesheet">
<style>
:root{
  --yellow:#fcc400;
  --yellow-deep:#f5b800;
  --charcoal:#4a4a4a;
  --ink:#111111;
  --hero:#262626;
  --footer:#242424;
  --footer-text:#c9c9c9;
  --panel:#e8e8e8;
  --green:#2db31f;
  --white:#ffffff;
}
*{margin:0;padding:0;box-sizing:border-box}
html,body{width:781px;height:1200px;overflow:hidden}
body{position:relative;background:var(--yellow);font-family:"Ubuntu",sans-serif;color:var(--ink)}
.abs{position:absolute}
.top-band{left:0;top:0;width:781px;height:335px;background:linear-gradient(#3f3f3f,#4d4d4d)}
.top-strip{left:0;top:0;width:781px;height:6px;background:var(--yellow)}
.quote-tab{left:515px;top:0;width:168px;height:54px;background:var(--yellow);border-radius:0 0 12px 12px;display:flex;align-items:center;padding-left:20px;gap:18px}
.quote-tab span{font-family:"Ubuntu",sans-serif;font-weight:500;font-size:15px;line-height:18px;color:var(--ink)}
.brand{left:80px;top:40px;width:140px;display:flex;align-items:center;gap:6px}
.brand-square{width:14px;height:14px;background:var(--yellow);flex:none}
.brand-name{font-size:11px;color:var(--white);font-weight:400;line-height:13px}
.main-nav{left:78px;top:113px;width:625px;height:34px;background:linear-gradient(var(--yellow),var(--yellow-deep));display:flex;justify-content:space-between;align-items:center;padding:0 18px}
.main-nav a{font-family:"Exo",sans-serif;font-weight:600;font-size:12px;color:var(--ink);text-decoration:none}
.hero{left:82px;top:147px;width:616px;height:244px;background:radial-gradient(ellipse at 40% 0%,#3a3a3a,var(--hero) 70%)}
.hero-strip{left:82px;top:332px;width:616px;height:59px;background:#111}
.hero-title{left:110px;top:180px;width:290px;font-family:"Exo",sans-serif;font-weight:600;font-size:16px;line-height:20px;color:var(--white)}
.hero-copy{left:110px;top:226px;width:274px;font-size:9.2px;line-height:12.2px;letter-spacing:-0.1px;color:var(--yellow)}
.hero-tagline{left:112px;top:352px;font-family:"Exo",sans-serif;font-weight:700;font-size:15px;color:var(--white)}
.hero-tagline em{font-style:normal;color:var(--yellow)}
.monitor{left:413px;top:202px;width:274px;height:211px}
.service{width:201px;text-align:center}
.service h3{font-family:"Exo",sans-serif;font-weight:700;font-size:11px;height:24px}
.service .visual{width:201px;height:134px;background:var(--white)}
.service p{margin-top:13px;font-size:8px;line-height:12.4px;letter-spacing:-0.15px;font-weight:500;height:62px}
.btn-dark{display:inline-block;width:72px;height:24px;line-height:24px;background:var(--ink);color:var(--yellow);font-size:8.5px;font-weight:500;text-align:center;border-radius:2px}
.service .btn-dark{margin-top:18px}
.divider{left:78px;top:782px;width:625px;height:3px;background:repeating-linear-gradient(90deg,#e0b24a 0 3px,transparent 3px 5px)}
.welcome-title{left:78px;top:822px;font-family:"Exo",sans-serif;font-weight:600;font-size:14px}
.welcome-copy{left:78px;top:850px;width:410px;font-size:8px;line-height:12.2px;letter-spacing:-0.1px;font-weight:500}
.welcome-btn{left:78px;top:953px}
.newsletter{left:501px;top:810px;width:202px;height:144px;background:var(--panel);border-top:3px solid #cfcfcf;padding:16px 15px}
.newsletter h4{font-family:"Exo",sans-serif;font-weight:700;font-size:12px}
.newsletter .sub{margin-top:7px;font-size:8px}
.field{margin-top:9px;width:162px;height:16px;background:var(--white);font-size:8px;color:#888;padding:3px 9px}
.field+.field{margin-top:8px}
.subscribe{margin-top:11px;width:66px;height:17px;background:var(--green);border:1px solid #1c7a12;color:var(--white);font-size:8px;text-align:center;line-height:15px}
.curl{right:0;bottom:0;width:36px;height:20px;background:linear-gradient(135deg,var(--panel) 50%,#bdbdbd 50%,#f5f5f5)}
.site-footer{left:0;top:1043px;width:781px;height:157px;background:var(--footer)}
.footer-heading{font-family:"Exo",sans-serif;font-weight:600;font-size:11px;color:var(--white)}
.link-list{list-style:none;font-size:8px;line-height:13px;color:var(--footer-text)}
.mission{left:548px;top:1072px;width:152px;font-size:8px;line-height:9.8px;color:var(--footer-text)}
.legal-links{left:78px;top:1156px;font-size:8px;color:var(--footer-text)}
.bottom-bar{left:0;top:1171px;width:781px;height:29px;background:#1b1b1b;border-top:1px solid #3a3a3a}
.copyright{left:0;top:1181px;width:781px;text-align:center;font-size:8px;color:var(--footer-text)}
.social{top:1179px;width:13px;height:13px;border-radius:50%;background:#5c5c5c}
</style>
</head>
<body>
<div class="abs top-band"></div>
<div class="abs top-strip"></div>

<a class="abs quote-tab">
  <svg width="28" height="26" viewBox="0 0 28 26" aria-hidden="true">
    <rect x="2" y="5" width="20" height="16" rx="2" fill="#4aa3df"/>
    <rect x="5" y="9" width="14" height="2" fill="#fff"/>
    <rect x="5" y="13" width="10" height="2" fill="#fff"/>
    <path d="M14 18 L24 4 L27 6 L17 20 Z" fill="#f06a2a"/>
  </svg>
  <span>Request<br>A Quote</span>
</a>

<div class="abs brand">
  <div class="brand-square"></div>
  <div class="brand-name">Brightlane Pixel Collective</div>
</div>

<nav class="abs main-nav">
  <a>HOME</a><a>WEB DESIGN</a><a>SEARCH ENGINE MARKETING</a><a>SOCIAL MEDIA</a><a>CONTACT</a>
</nav>

<section class="abs hero"></section>
<div class="abs hero-strip"></div>
<h1 class="abs hero-title">Brightlane Pixel Collective will get you noticed</h1>
<p class="abs hero-copy">We are an award winning web design &amp; internet marketing company located in Minneapolis. As a Minneapolis Web Design company, we create web sites to what our clients want and that's found in our marketing. Here at Brightlane Pixel Collective, we not only design you a first class web presence but market your website so your buyer finds you first before anyone else.</p>
<h2 class="abs hero-tagline">WE ARE <em>SEO</em> SPECIALIST</h2>

<svg class="abs monitor" viewBox="0 0 274 211" role="img" aria-label="Desktop monitor showing an analytics dashboard">
  <rect x="0" y="0" width="274" height="176" rx="4" fill="#111"/>
  <rect x="8" y="8" width="258" height="160" fill="#e4e6ea"/>
  <path d="M108 176 L166 176 L172 200 L102 200 Z" fill="#cfd2d6"/>
  <ellipse cx="137" cy="203" rx="50" ry="7" fill="#e9ebee"/>
</svg>

<div class="abs service" style="left:78px;top:451px">
  <h3>SEARCH ENGINE OPTIMIZATION</h3>
  <div class="visual" role="img" aria-label="Illustration of a chart board, money symbol and businessman" style="background:linear-gradient(135deg,#ffffff,#e9efe6)"></div>
  <p>Lorem ipsum dolor sit amet, consectetuer adipiscing elit, sed diam nonummy nibh euismod tinacidunt ut laoreet dolore magna aliquaam erat volutpat. Ut wisi eanim ad minim veniam, quis nosatrud exerci tation ullaamcorper susacipit loborsati saliaqauip odo consequat.</p>
  <a class="btn-dark">Read More</a>
</div>
<div class="abs service" style="left:290px;top:451px">
  <h3>SOCIAL MEDIA MARKETING</h3>
  <div class="visual" role="img" aria-label="Word cloud about social media" style="background:linear-gradient(135deg,#ffffff,#eef1f6)"></div>
  <p>Lorem ipsum dolor sit amet, consectetuer adipiscing elit, sed diam nonummy nibh euismod tinacidunt ut laoreet dolore magna aliquaam erat volutpat. Ut wisi eanim ad minim veniam, quis nosatrud exerci tation ullaamcorper susacipit loborsati saliaqauip odo consequat.</p>
  <a class="btn-dark">Read More</a>
</div>
<div class="abs service" style="left:501px;top:451px">
  <h3>WEB DESIGN</h3>
  <div class="visual" role="img" aria-label="Website design artwork with palette icon" style="background:linear-gradient(135deg,#ffffff,#eef3f8)"></div>
  <p>Lorem ipsum dolor sit amet, consectetuer adipiscing elit, sed diam nonummy nibh euismod tinacidunt ut laoreet dolore magna aliquaam erat volutpat. Ut wisi eanim ad minim veniam, quis nosatrud exerci tation ullaamcorper susacipit loborsati saliaqauip odo consequat.</p>
  <a class="btn-dark">Read More</a>
</div>

<div class="abs divider"></div>

<h2 class="abs welcome-title">WELCOME TO BRIGHTLANE PIXEL COLLECTIVE</h2>
<p class="abs welcome-copy">Lorem ipsum dolor sit amet, consectetuer adipiscing elit, sed diam nonummy nibh euismod tinacidunt ut laoreet dolore magna aliquaam erat volutpat. Ut wisi eanim ad minim veniam, quis nosatrud exerci tation ullaamcorper susacipit loborsatis nisl ut aaliaqauip ex esa commodo consequat. Lorem ipsum dolor sit amet, consectetuer adipiscing elit, sed diam nonummy nibh euismod tinacidunt ut laoreet dolore magna aliquaam erat volutpat. Ut wisi eanim ad minim veniam, quis nosatrud exerci tation ullaamcorper susacipit loborsatis nisl ut aaliaqauip ex esa tinacidunt ut laoreet dolore magna aliquaam erat volutpat. Ut wisi eanim ad minim veniam, quis nosatrud exerci tation ullaamcorper susacipit loborsatis nisl ut aaliaqauip ex esa commodo consequat.</p>
<a class="abs btn-dark welcome-btn">Read More</a>

<aside class="abs newsletter">
  <h4>SUBSCRIBE TO NEWSLETTERS</h4>
  <div class="sub">Subscribe to our weekly newsletters</div>
  <div class="field">Your Name</div>
  <div class="field">Your Email</div>
  <div class="subscribe">Subscribe</div>
  <div class="abs curl"></div>
</aside>

<footer class="abs site-footer"></footer>
<div class="abs footer-heading" style="left:78px;top:1054px">Sitemap</div>
<ul class="abs link-list" style="left:78px;top:1071px"><li>Home</li><li>Web Design</li><li>Search Engine Marketing</li><li>Social Media</li><li>Contact</li></ul>
<ul class="abs link-list" style="left:234px;top:1071px"><li>Local Map Listings</li><li>National SEO</li><li>Learn SEO</li><li>Website Design</li><li>Client Controlled Website</li></ul>
<ul class="abs link-list" style="left:377px;top:1071px"><li>Animated Website</li><li>Build an E-commerce Site</li><li>Video Channel Optimization</li><li>Graphic Design</li><li>Logo Design</li></ul>
<div class="abs footer-heading" style="left:548px;top:1054px">Our Mission</div>
<p class="abs mission">We are an award winning web design &amp; internet marketing company located in Minneapolis. As a Minneapolis Web Design company, we create web sites to what our clients want and that's found in our marketing.</p>
<div class="abs legal-links">Home | Privacy Policy | Refund Policy | Terms &amp; Conditions | About | Affiliates | Contact</div>
<div class="abs bottom-bar"></div>
<div class="abs copyright">© 2009-2013 Brightlane Pixel Collective, Inc. All rights reserved.</div>
<div class="abs social" style="left:637px"></div>
<div class="abs social" style="left:663px"></div>
<div class="abs social" style="left:689px"></div>
</body>
</html>
```